logo & Business Card Design

NovaGuard Termite & Pest Control, I need a great logo, take my ideas and run with them!
I will use this in marketing and website so needs to be eye catching but professional

Target Market(s)

Resedintial & Business

Industry/Entity Type

Marketing

Contact Information for Business Card

Need front side with pertinent info & Logo; back side will have a 25% off initial services Coupon!

Font styles to use
Sans Serif

Colors
ec1f27
1b1b1b

Requirements
Must have
• Professional logo and style
Nice to have
• Raised lettering, black, red, white colors maybe? I'm flexible, but those colors go good on any background, vehicle, uniform, etc...
Should not have
• Cheesy

```html
<!DOCTYPE html>
<html lang="en">
<head>
<meta charset="utf-8">
<title>NovaGuard Termite &amp; Pest Control – Logo &amp; Business Card</title>
<link rel="stylesheet" href="https://fonts.googleapis.com/css2?family=Roboto+Condensed:wght@400;700&display=swap">
<style>
  :root {
    --stage-top: #e4e4e4;
    --stage-bottom: #fbfbfb;
    --card-dark: #5a0a0e;
    --card-mid: #8c1218;
    --card-light: #b71c22;
    --brand-red: #ec1f27;
    --brand-black: #1b1b1b;
    --gold: #e9b43a;
    --orange: #ee7a1c;
    --white: #ffffff;
  }
  * { margin: 0; padding: 0; box-sizing: border-box; }
  html, body { width: 1200px; height: 450px; overflow: hidden; }
  body {
    font-family: "Roboto Condensed", Arial, sans-serif;
    background: linear-gradient(180deg, var(--stage-top), var(--stage-bottom));
    position: relative;
  }

  /* ---------- Business card front ---------- */
  .card {
    position: absolute;
    left: 60px; top: 60px;
    width: 540px; height: 327px;
    background: linear-gradient(180deg, var(--card-dark) 0%, var(--card-mid) 45%, var(--card-light) 100%);
    box-shadow: 0 2px 6px rgba(0,0,0,0.25);
    color: var(--white);
  }
  .card-brand {
    position: absolute;
    left: 52px; top: 60px;
    display: flex; align-items: center; gap: 18px;
  }
  .card-brand-mark {
    width: 74px; height: 74px; border-radius: 50%;
    background: var(--gold);
    flex: none;
  }
  .card-brand-name {
    color: var(--gold);
    font-weight: 700;
    text-transform: uppercase;
    line-height: 1.05;
  }
  .card-brand-name .line1 { display: block; font-size: 34px; letter-spacing: 1.5px; }
  .card-brand-name .line2 { display: block; font-size: 20px; letter-spacing: 0.5px; }

  .tagline {
    position: absolute;
    left: 195px; top: 128px;
    font-size: 13.5px; font-weight: 700;
    text-transform: uppercase;
  }
  .person {
    position: absolute;
    left: 135px; top: 166px;
    width: 180px;
  }
  .person-name { font-size: 22px; font-weight: 400; text-transform: uppercase; letter-spacing: 0.3px; }
  .person-title {
    font-size: 14px; color: var(--gold); text-transform: uppercase;
    text-align: right; margin-top: 1px;
  }
  .contact {
    position: absolute;
    left: 120px; top: 220px;
    list-style: none;
    font-size: 15px;
  }
  .contact li { display: flex; align-items: center; gap: 8px; height: 25px; }
  .contact .email { font-size: 12.5px; }
  .contact-icon {
    width: 16px; height: 16px; border-radius: 50%;
    background: var(--gold);
    display: flex; align-items: center; justify-content: center;
    flex: none;
  }
  .website {
    position: absolute;
    left: 102px; top: 272px;
    font-size: 12.5px; text-transform: uppercase;
  }

  /* ---------- Standalone logo ---------- */
  .logo-lockup {
    position: absolute;
    left: 757px; top: 52px;
    width: 300px;
    display: flex; flex-direction: column; align-items: center;
  }
  .logo-name {
    color: var(--orange);
    font-weight: 700;
    text-transform: uppercase;
    text-align: center;
    line-height: 1.05;
  }
  .logo-name .line1 { display: block; font-size: 46px; letter-spacing: 2px; }
  .logo-name .line2 { display: block; font-size: 26px; }
  .logo-mark {
    margin-top: 36px;
    width: 190px; height: 190px; border-radius: 50%;
    background: var(--orange);
  }
</style>
</head>
<body>

  <section class="card" aria-label="Business card front">
    <div class="card-brand">
      <span class="card-brand-mark" aria-hidden="true"></span>
      <h1 class="card-brand-name">
        <span class="line1">NovaGuard</span>
        <span class="line2">Termite &amp; Pest Control</span>
      </h1>
    </div>

    <p class="tagline">A shield of protection for your home or business</p>

    <div class="person">
      <p class="person-name">Daniel Brooks</p>
      <p class="person-title">President</p>
    </div>

    <ul class="contact">
      <li>
        <span class="contact-icon">
          <svg width="10" height="10" viewBox="0 0 24 24" aria-hidden="true"><path fill="#5a0a0e" d="M6.6 10.8a15.1 15.1 0 0 0 6.6 6.6l2.2-2.2a1 1 0 0 1 1-.25 11.4 11.4 0 0 0 3.6.57 1 1 0 0 1 1 1V20a1 1 0 0 1-1 1A17 17 0 0 1 3 4a1 1 0 0 1 1-1h3.5a1 1 0 0 1 1 1c0 1.25.2 2.45.57 3.57a1 1 0 0 1-.25 1z"/></svg>
        </span>
        <span>251-555-0148</span>
      </li>
      <li class="email">
        <span class="contact-icon">
          <svg width="10" height="10" viewBox="0 0 24 24" aria-hidden="true"><path fill="#5a0a0e" d="M2 5h20v14H2z"/><path fill="none" stroke="#e9b43a" stroke-width="2" d="M2 5l10 8 10-8"/></svg>
        </span>
        <span>DAN@NOVAGUARDPEST.COM</span>
      </li>
    </ul>

    <p class="website">www.novaguardpestcontrol.com</p>
  </section>

  <section class="logo-lockup" aria-label="NovaGuard logo">
    <h2 class="logo-name">
      <span class="line1">NovaGuard</span>
      <span class="line2">Termite &amp; Pest Control</span>
    </h2>
    <span class="logo-mark" aria-hidden="true"></span>
  </section>

</body>
</html>
```